I own a rendering company which is in the construction industry i already have a logo i would like i

I want to make the website look professional and blends nicely with the logo, if i can have contact information and photos logos and a place where they can email me for job quotes or request and we want to win the big jobs so think also corporate in conjunction with construction. also an area for brief description and about us

Target Market(s)

Home owners/Investors, Small and major construction companies

Industry/Entity Type

Construction Company

Coding

Coded - Design and coding required

Number of Pages Required

3 page

Font styles to use
Serif
Sans Serif

Colors

Designer to choose colors to be used in the design.

Requirements
Must have
• An area for pictures to show with fade changes or clicking options(of white set walls, acrylic render expensive houses walls) an "about us" section. An area to where potential customers can email us (a writing box) where we can receive request for quotes and potential jobs. all contact information and license numbers
Nice to have
• pictures of plastered walls (posh elegant) and rendered walls acrylic and cement render
Should not have
• anything boring plain font etc

```html
<!DOCTYPE html>
<html lang="en">
<head>
<meta charset="utf-8">
<title>Falcrest Rendering</title>
<link rel="stylesheet" href="https://fonts.googleapis.com/css2?family=Cinzel:wght@400;700&family=Open+Sans:wght@400;600;700&display=swap">
<style>
:root{
  --red:#e31e24;
  --ink:#222222;
  --text:#555555;
  --grey-band:#7b7b7b;
  --grey-nav:#8a8a8a;
  --grey-line:#b5b5b5;
  --footer:#333333;
  --footer-deep:#232323;
  --field:#4a4a4a;
  --white:#ffffff;
  --map-link:#1a4f9c;
}
*{box-sizing:border-box;margin:0;padding:0}
html,body{width:1200px;height:3629px;overflow:hidden;background:var(--white)}
body{position:relative;font-family:"Open Sans",Arial,sans-serif;color:var(--text)}
.abs{position:absolute;z-index:2}
.media{position:absolute;display:block}

/* header */
.site-header{position:absolute;left:0;top:0;width:1200px;height:140px;background:var(--white);z-index:3}
.brand{position:absolute;left:40px;top:28px;width:170px;color:var(--red);font-weight:700;font-size:28px;line-height:30px;letter-spacing:1px;text-align:center}
.brand .brand-mark{display:block;width:26px;height:26px;background:var(--red);margin:0 auto 8px;border-radius:50%}
.brand small{display:block;font-size:17px;font-weight:700;letter-spacing:4px;line-height:20px}
.quick-contact{position:absolute;top:26px;display:flex;align-items:center;gap:12px}
.quick-contact svg{width:28px;height:34px}
.quick-contact .label{font-size:9px;letter-spacing:1px;color:#777;text-transform:uppercase;line-height:12px}
.quick-contact .value{font-size:15px;font-weight:600;color:var(--ink);line-height:20px}
.main-nav{position:absolute;left:262px;top:87px;width:938px;height:53px;background:var(--grey-nav);clip-path:polygon(30px 0,100% 0,100% 100%,0 100%)}
.main-nav a{position:absolute;top:0;line-height:53px;color:var(--white);font-size:15px;font-weight:600;text-decoration:none;letter-spacing:.5px}
.main-nav a.active::after{content:"";position:absolute;left:-6px;right:-6px;bottom:0;height:4px;background:var(--red)}
.main-nav svg{position:absolute;left:880px;top:16px}

/* hero */
.hero{position:absolute;left:0;top:140px;width:1200px;height:660px;z-index:1}
.hero .media{left:0;top:0;width:1200px;height:650px;background:linear-gradient(160deg,#f2c79a 0%,#9eb2c9 22%,#5f7897 48%,#2f3a4c 72%,#6c6258 100%)}
.hero svg.swoosh{position:absolute;left:0;top:420px}

/* about */
.about-photo-main{left:121px;top:755px;width:364px;height:310px;background:linear-gradient(160deg,#5f94d2 0%,#a9c7e6 30%,#f3f4f5 55%,#c9ccce 80%,#3f5b7a 100%);z-index:2}
.about-photo-frame{position:absolute;left:145px;top:780px;width:320px;height:255px;border:3px solid var(--white);z-index:2}
.about-photo-small{left:317px;top:980px;width:230px;height:201px;background:linear-gradient(150deg,#d9d2c4 0%,#9b8a72 45%,#6a5a48 100%);border:4px solid var(--white);z-index:2}
.section-title{font-family:"Cinzel",Georgia,serif;font-weight:400;letter-spacing:2px}
.about-title{left:634px;top:842px;font-size:50px;color:var(--red)}
.body-copy{font-size:15px;line-height:29px;color:var(--text)}
.about-copy{left:634px;top:914px;width:500px}

/* services */
.services{position:absolute;left:0;top:1282px;width:1200px;height:636px;background:var(--grey-band)}
.services-title{position:absolute;left:0;width:100%;top:32px;text-align:center;font-size:40px;color:var(--white)}
.service{position:absolute;top:128px;width:340px;text-align:center;color:var(--white)}
.service .ring{width:252px;height:252px;border-radius:50%;border:12px solid #c8c8c8;margin:0 auto;padding:8px;background:var(--grey-band)}
.service.featured .ring{border-color:var(--red)}
.service .ring .media{position:relative;width:100%;height:100%;border-radius:50%}
.service h3{margin-top:26px;font-family:Arial,"Open Sans",sans-serif;font-weight:700;font-size:20px;line-height:24px;text-transform:uppercase}
.service p{margin:10px auto 0;width:270px;font-size:14px;line-height:18px;color:#f2f2f2}
.service .more{display:block;margin:26px auto 0;width:34px;height:34px}

/* works */
.works-title{left:0;width:1200px;top:1953px;text-align:center;font-size:42px;color:var(--ink)}
.filter{position:absolute;top:2044px;height:37px;border:2px solid #c9c9c9;background:var(--white);color:#444;font-size:14px;line-height:33px;text-align:center;text-transform:uppercase}
.filter.active{background:var(--red);border-color:var(--red);color:var(--white)}
.gallery{position:absolute;left:0;top:2124px;width:1200px;height:448px;display:grid;grid-template-columns:repeat(5,240px);grid-template-rows:224px 224px}
.gallery .media{position:relative}

/* who we are */
.who-title{left:53px;top:2684px;font-size:50px;color:var(--red)}
.who-copy{left:53px;top:2756px;width:510px}
.video{position:absolute;left:624px;top:2676px;width:511px;height:314px;background:#3c3c3c}
.video .video-name{position:absolute;left:0;width:100%;top:176px;text-align:center;font-weight:700;font-size:36px;letter-spacing:3px;color:#8e8e8e}
.video svg{position:absolute;left:218px;top:82px}

/* footer */
.footer-wave{position:absolute;left:0;top:3040px;z-index:2}
.footer{position:absolute;left:0;top:3180px;width:1200px;height:400px;background:var(--footer);z-index:1}
.contact-title{position:absolute;left:53px;top:10px;font-size:36px;color:var(--white)}
.field{position:absolute;background:var(--field);color:#9a9a9a;font-size:12px;padding:0 12px;line-height:34px}
.submit{position:absolute;left:56px;top:292px;width:406px;height:43px;background:var(--red);color:var(--white);font-weight:600;font-size:15px;text-align:center;line-height:43px;letter-spacing:1px}
.address{position:absolute;left:530px;color:#e6e6e6;font-size:14px;line-height:23px;z-index:3}
.address h4{font-size:15px;font-weight:700;color:var(--white);margin-bottom:6px}
.map{position:absolute;left:842px;top:115px;width:266px;height:215px;border:4px solid #e8e8e8;background:linear-gradient(135deg,#eceae4 0%,#dfe6d6 55%,#cfd8e4 100%)}
.map-link{position:absolute;left:852px;top:304px;font-size:11px;color:var(--map-link);text-decoration:underline}
.copyright{position:absolute;left:0;top:3580px;width:1200px;height:49px;background:var(--footer-deep);color:#bdbdbd;font-size:12px;text-align:center;line-height:49px}
</style>
</head>
<body>

<header class="site-header">
  <div class="brand"><span class="brand-mark"></span>FALCREST<small>RENDERING</small></div>

  <div class="quick-contact" style="left:708px">
    <svg viewBox="0 0 28 34" aria-hidden="true"><rect x="7" y="2" width="14" height="28" rx="2" fill="none" stroke="#555" stroke-width="2"/><circle cx="14" cy="26" r="1.5" fill="#555"/></svg>
    <div><div class="label">Call us today</div><div class="value">555-014-2290</div></div>
  </div>
  <div class="quick-contact" style="left:900px">
    <svg viewBox="0 0 34 34" aria-hidden="true" style="width:34px"><rect x="2" y="8" width="30" height="20" fill="none" stroke="#555" stroke-width="2"/><path d="M2 8 L17 20 L32 8" fill="none" stroke="#555" stroke-width="2"/></svg>
    <div><div class="label">Email us now</div><div class="value">info@falcrestrendering.com</div></div>
  </div>

  <nav class="main-nav">
    <a class="active" style="left:89px">HOME</a>
    <a style="left:186px">ABOUT</a>
    <a style="left:289px">SERVICES</a>
    <a style="left:408px">PROJECTS</a>
    <a style="left:530px">BLOG</a>
    <a style="left:623px">CONTACT</a>
    <svg width="14" height="20" viewBox="0 0 14 20" aria-hidden="true"><path d="M7 0C3 0 0 3 0 7c0 5 7 13 7 13s7-8 7-13c0-4-3-7-7-7z" fill="#fff"/><circle cx="7" cy="7" r="2.5" fill="#8a8a8a"/></svg>
  </nav>
</header>

<section class="hero">
  <div class="media" role="img" aria-label="Modern glass high-rise building at dusk with city skyline"></div>
  <svg class="swoosh" width="1200" height="240" viewBox="0 0 1200 240" aria-hidden="true">
    <path d="M0 45 C400 90 800 200 1200 195 L1200 240 L0 240 Z" fill="#ffffff"/>
    <path d="M0 12 C300 20 700 70 1200 90 L1200 195 C800 200 400 90 0 45 Z" fill="#e31e24"/>
    <path d="M0 51 C400 96 800 206 1200 201 L1200 210 C800 215 400 105 0 60 Z" fill="#b5b5b5"/>
  </svg>
</section>

<div class="media about-photo-main" role="img" aria-label="White rendered modular building under blue sky"></div>
<div class="about-photo-frame"></div>
<div class="media about-photo-small" role="img" aria-label="Plasterer rendering an interior wall"></div>
<h2 class="abs section-title about-title">ABOUT US</h2>
<p class="abs body-copy about-copy">Anyone can sue a Debtor. Nor, is it difficult to get nasty or treat people who owe you money in a rude and unprofessional way. However, very few people have the skill, temperament and experience necessary to effectively negotiate with Debtors, stakeholders, lawyers, as well as, court personnel, sheriffs and bankers to efficiently collect the most money possible in the least amount of time.</p>

<section class="services">
  <h2 class="section-title services-title">OUR SERVICES</h2>
  <div class="service featured" style="left:65px">
    <div class="ring"><div class="media" role="img" aria-label="Worker installing roof panels" style="background:linear-gradient(160deg,#d8c2b4 0%,#a57d6a 40%,#c8aca0 65%,#7d5e52 100%)"></div></div>
    <h3>Property Acquisitions and<br>Feasibility Studies</h3>
    <p>Lorem ipsum dolor sit amet, consectetuer adipiscing elit. Aenean commodo ligula eget dolor. Aenean massa. Cum sociis natoque.</p>
    <svg class="more" viewBox="0 0 34 34" aria-hidden="true"><circle cx="17" cy="17" r="17" fill="#333"/><path d="M17 10v14M10 17h14" stroke="#fff" stroke-width="2.5"/></svg>
  </div>
  <div class="service" style="left:442px">
    <div class="ring"><div class="media" role="img" aria-label="Roofer laying shingles" style="background:linear-gradient(160deg,#4f8a3e 0%,#6f9a52 25%,#6d6c6a 50%,#3f3e3d 100%)"></div></div>
    <h3>Architecture and<br>Engineering Services</h3>
    <p>Lorem ipsum dolor sit amet, consectetuer adipiscing elit. Aenean commodo ligula eget dolor. Aenean massa. Cum sociis natoque.</p>
    <svg class="more" viewBox="0 0 34 34" aria-hidden="true"><circle cx="17" cy="17" r="17" fill="#333"/><path d="M17 10v14M10 17h14" stroke="#fff" stroke-width="2.5"/></svg>
  </div>
  <div class="service" style="left:805px">
    <div class="ring"><div class="media" role="img" aria-label="Worker cutting boards on a rooftop" style="background:linear-gradient(160deg,#7a9cc8 0%,#4b6283 30%,#3b3c40 60%,#e0c48e 100%)"></div></div>
    <h3>3D Renderings and<br>Visualization Design</h3>
    <p>Lorem ipsum dolor sit amet, consectetuer adipiscing elit. Aenean commodo ligula eget dolor. Aenean massa. Cum sociis natoque.</p>
    <svg class="more" viewBox="0 0 34 34" aria-hidden="true"><circle cx="17" cy="17" r="17" fill="#333"/><path d="M17 10v14M10 17h14" stroke="#fff" stroke-width="2.5"/></svg>
  </div>
</section>

<h2 class="abs section-title works-title">COMPLETED WORKS</h2>
<div class="filter active" style="left:339px;width:104px">All</div>
<div class="filter" style="left:464px;width:117px">Bathroom</div>
<div class="filter" style="left:600px;width:116px">Kitchen</div>
<div class="filter" style="left:728px;width:133px">Installation</div>

<div class="gallery">
  <div class="media" role="img" aria-label="Nail gun fixing roof shingles" style="background:linear-gradient(150deg,#c9a15a 0%,#7d7a74 45%,#9aa3a8 100%)"></div>
  <div class="media" role="img" aria-label="Worker fitting floor panels" style="background:linear-gradient(150deg,#3e362f 0%,#8a7c6c 50%,#c4b8a6 100%)"></div>
  <div class="media" role="img" aria-label="Roofer on a pitched roof" style="background:linear-gradient(150deg,#d9d3c7 0%,#8a7b68 55%,#4f463d 100%)"></div>
  <div class="media" role="img" aria-label="Workers insulating an exterior wall" style="background:linear-gradient(150deg,#d6b47a 0%,#a88d62 50%,#7e8d8f 100%)"></div>
  <div class="media" role="img" aria-label="Roofer laying shingles near houses" style="background:linear-gradient(150deg,#a9c4e0 0%,#d8d4c9 35%,#b35e45 70%,#8a4a38 100%)"></div>
  <div class="media" role="img" aria-label="Bright modern living room interior" style="background:linear-gradient(150deg,#f4f3ef 0%,#cfcbc2 50%,#6c6b67 100%)"></div>
  <div class="media" role="img" aria-label="Office interior with ceiling lights" style="background:linear-gradient(150deg,#1f1d1b 0%,#5a5149 45%,#d6cfc2 100%)"></div>
  <div class="media" role="img" aria-label="Bricklayer building a block wall" style="background:linear-gradient(150deg,#5a4b40 0%,#b7b0a4 50%,#8e8579 100%)"></div>
  <div class="media" role="img" aria-label="Roofer working among trees" style="background:linear-gradient(150deg,#4e8a3f 0%,#8fb07a 30%,#4b4a4c 65%,#6a6a6e 100%)"></div>
  <div class="media" role="img" aria-label="Carpenter measuring timber outdoors" style="background:linear-gradient(150deg,#7faedc 0%,#b7d0e6 40%,#e6cf9e 70%,#c9a56a 100%)"></div>
</div>

<h2 class="abs section-title who-title">WHO WE ARE</h2>
<p class="abs body-copy who-copy">Anyone can sue a Debtor. Nor, is it difficult to get nasty or treat people who owe you money in a rude and unprofessional way. However, very few people have the skill, temperament and experience necessary to effectively negotiate with Debtors, stakeholders, lawyers, as well as, court personnel, sheriffs and bankers to efficiently collect the most money possible in the least amount of time.</p>

<div class="video" role="img" aria-label="Company introduction video">
  <svg width="76" height="76" viewBox="0 0 76 76" aria-hidden="true"><circle cx="38" cy="38" r="38" fill="#e31e24"/><path d="M30 24 L54 38 L30 52 Z" fill="#3c3c3c"/></svg>
  <div class="video-name">FALCREST RENDERING</div>
</div>

<svg class="footer-wave" width="1200" height="230" viewBox="0 0 1200 230" aria-hidden="true">
  <path d="M0 28 C400 30 800 50 1200 70 L1200 230 L0 230 Z" fill="#333333"/>
  <path d="M0 15 C400 20 800 80 1200 160 L1200 210 C800 120 400 50 0 40 Z" fill="#e31e24"/>
  <path d="M0 40 C400 50 800 120 1200 210 L1200 215 C800 125 400 55 0 45 Z" fill="#ffffff"/>
  <path d="M0 45 C400 55 800 125 1200 215 L1200 223 C800 133 400 63 0 53 Z" fill="#b5b5b5"/>
</svg>

<footer class="footer">
  <h2 class="section-title contact-title">CONTACT US</h2>
  <div class="field" style="left:56px;top:91px;width:193px">Name</div>
  <div class="field" style="left:269px;top:91px;width:193px">Email</div>
  <div class="field" style="left:56px;top:144px;width:193px">Phone</div>
  <div class="field" style="left:269px;top:144px;width:193px">Subject</div>
  <div class="field" style="left:56px;top:197px;width:406px;height:75px">Message</div>
  <div class="submit">SUBMIT</div>

  <div class="address" style="top:108px">
    <h4>Office Address</h4>
    412 Harwood Avenue<br>Suite 210<br>Millbrook, New York 10590
  </div>
  <div class="address" style="top:234px">
    <h4>Mailing Address</h4>
    96 Linden Street South<br>Suite 1180<br>New York, NY 10012
  </div>

  <div class="map" role="img" aria-label="Street map showing the office location"></div>
  <span class="map-link">View Larger Map</span>
</footer>

<div class="copyright">Copyright © 2018 Falcrest Rendering | All Right Reserved</div>

</body>
</html>
```